Create a Eye Catching Flyerr for my online business

I would like an eye catching flyer with the relevant content for my business.

This flyer is to advertise my online business and the call to action is to get Butchers to sign up to my online site to start selling their products.

the flyer must be eye catching, each to understand, easy to read and relevant to the audience being local butcher shops.

Attached is the marketing packs with all the required information about the business The flyer must not be too long, but the front page must be catching and want the audience to read more. It must very direct, targeted and focused on the audience

It mus be duplicate sides

Industry/Entity Type

Marketing

Font styles to use
Serif
Sans Serif

Colors
9bcb3b
ffffff
fee18a
fac994
f37122
f78f20
ffc214

```html
<!DOCTYPE html>
<html lang="en">
<head>
<meta charset="utf-8">
<title>Catch &amp; Cut Market – Flyer</title>
<link rel="stylesheet" href="https://fonts.googleapis.com/css2?family=Oswald:wght@500&family=Raleway:wght@400;700&family=Arimo:wght@700&family=Archivo+Black&display=swap">
<style>
  :root{
    --green:#6b9a3a;
    --green-dark:#4f7a27;
    --orange:#e8702e;
    --orange-dark:#d85e1c;
    --paper-top:#f4f4f4;
    --paper-bottom:#dcdcdc;
    --ink:#111;
    --stage:#2a2a2a;
    --white:#fff;
  }
  html,body{margin:0;padding:0;overflow:hidden;background:var(--stage);}
  .stage{position:relative;width:1200px;height:900px;overflow:hidden;background:var(--stage);}
  .page{position:absolute;overflow:hidden;background:linear-gradient(180deg,var(--paper-top),var(--paper-bottom));}
  .page svg.shapes{position:absolute;left:0;top:0;width:100%;height:100%;}
  .page--front{left:55px;top:70px;width:533px;height:754px;}
  .page--back{left:623px;top:70px;width:532px;height:750px;}

  /* front */
  .brand{position:absolute;left:28px;top:298px;font-family:"Raleway",sans-serif;font-weight:700;font-size:17px;letter-spacing:1px;color:#333;}
  .offer{position:absolute;left:45px;width:378px;margin:0;color:var(--white);font-family:"Raleway",sans-serif;font-size:14px;line-height:17px;}
  .offer b{font-family:"Oswald",sans-serif;font-weight:500;font-size:26px;letter-spacing:.2px;}
  .offer--shop{top:357px;}
  .offer--orders{top:470px;}
  .offer--customers{top:583px;}

  /* back */
  .benefits-title{position:absolute;left:14px;top:286px;margin:0;font-family:"Archivo Black",sans-serif;font-size:31px;color:var(--green);letter-spacing:.5px;text-shadow:1px 1px 0 #fff,2px 2px 2px rgba(0,0,0,.25);}
  .benefits{position:absolute;left:0;top:328px;width:360px;height:217px;background:var(--green);border-radius:0 60px 60px 0;margin:0;padding:18px 30px 0 16px;box-sizing:border-box;list-style:none;box-shadow:0 6px 8px rgba(0,0,0,.18);}
  .benefits li{position:relative;padding-left:22px;margin-bottom:9px;font-family:"Arimo",sans-serif;font-weight:700;font-size:14.5px;line-height:21px;color:var(--white);}
  .benefits li svg{position:absolute;left:0;top:5px;}
  .note{position:absolute;left:12px;top:560px;width:515px;margin:0;font-family:"Arimo",sans-serif;font-weight:700;font-size:14.2px;line-height:24px;color:var(--ink);}
  .sticker{position:absolute;left:390px;top:292px;width:124px;height:124px;border-radius:50%;background:radial-gradient(circle at 35% 30%,#f08a4a,var(--orange) 60%,var(--orange-dark));box-shadow:2px 3px 6px rgba(0,0,0,.3);}
  .sticker p{position:absolute;left:10px;top:40px;width:110px;margin:0;transform:rotate(-38deg);text-align:center;font-family:"Arimo",sans-serif;font-weight:700;font-size:13px;line-height:14px;color:var(--white);}
  .sticker strong{font-size:15px;}
  .cta{position:absolute;left:0;bottom:6px;width:100%;text-align:center;font-family:"Arimo",sans-serif;font-weight:700;color:var(--white);}
  .cta h2{margin:0;font-size:15px;line-height:17px;letter-spacing:.3px;}
  .cta p{margin:0;font-size:14px;line-height:16px;}
</style>
</head>
<body>
<div class="stage">

  <!-- Front side -->
  <section class="page page--front">
    <svg class="shapes" viewBox="0 0 533 754">
      <defs>
        <radialGradient id="steakTone" cx="55%" cy="55%" r="70%">
          <stop offset="0" stop-color="#c23a2e"/>
          <stop offset=".45" stop-color="#a8302a"/>
          <stop offset=".8" stop-color="#e9d6cf"/>
          <stop offset="1" stop-color="#fbf7f4"/>
        </radialGradient>
        <radialGradient id="dicedTone" cx="45%" cy="40%" r="65%"><stop offset="0" stop-color="#d8553f"/><stop offset="1" stop-color="#8f2a26"/></radialGradient>
        <radialGradient id="fishTone" cx="45%" cy="40%" r="65%"><stop offset="0" stop-color="#e3e6ea"/><stop offset="1" stop-color="#7d8792"/></radialGradient>
        <radialGradient id="cubedTone" cx="45%" cy="40%" r="65%"><stop offset="0" stop-color="#e07a7e"/><stop offset="1" stop-color="#a63a45"/></radialGradient>
        <radialGradient id="badgeTone" cx="40%" cy="35%" r="70%"><stop offset="0" stop-color="#8cbf52"/><stop offset="1" stop-color="var(--green-dark)"/></radialGradient>
        <filter id="soft" x="-10%" y="-10%" width="120%" height="140%"><feDropShadow dx="0" dy="5" stdDeviation="4" flood-opacity=".22"/></filter>
      </defs>
      <path d="M95,0 H150 Q145,215 290,270 Q420,305 533,292 V318 Q400,338 262,298 Q105,240 95,0Z" fill="var(--green)"/>
      <path role="img" aria-label="Photo of raw beef steaks with basil leaves and a scoop of peppercorns" d="M150,0 H533 V288 Q420,300 290,266 Q150,212 150,0Z" fill="url(#steakTone)"/>
      <circle cx="130" cy="205" r="80" fill="url(#badgeTone)" stroke="#fff" stroke-width="3"/>
      <path d="M0,650 Q260,705 533,690 V754 H0Z" fill="var(--orange)"/>
      <rect x="442" y="323" width="68" height="350" rx="6" fill="var(--green)" stroke="#fff" stroke-width="3"/>
      <g filter="url(#soft)">
        <path d="M55,348 H480 V428 H55 A40,40 0 0 1 55,348Z" fill="var(--green)"/>
        <path d="M55,460 H480 V540 H55 A40,40 0 0 1 55,460Z" fill="var(--green)"/>
        <path d="M55,573 H480 V653 H55 A40,40 0 0 1 55,573Z" fill="var(--green)"/>
      </g>
      <circle role="img" aria-label="Photo of diced red meat" cx="470" cy="385" r="44" fill="url(#dicedTone)" stroke="#fff" stroke-width="4"/>
      <circle role="img" aria-label="Photo of whole fresh fish" cx="470" cy="497" r="44" fill="url(#fishTone)" stroke="#fff" stroke-width="4"/>
      <circle role="img" aria-label="Photo of cubed beef" cx="470" cy="610" r="44" fill="url(#cubedTone)" stroke="#fff" stroke-width="4"/>
    </svg>
    <div class="brand">CATCH &amp; CUT MARKET</div>
    <p class="offer offer--shop"><b>WE OFFER</b> an easily managed online shop for<br>your business.The solution is customised specifically for<br>the Meat &amp; Fish industry.</p>
    <p class="offer offer--orders"><b>YOU GET</b> fully paid orders before they are<br>picked up or delivered</p>
    <p class="offer offer--customers"><b>CUSTOMERS BENEFIT</b> is from the convince of<br>ordering your quality products online 24x7</p>
  </section>

  <!-- Back side -->
  <section class="page page--back">
    <svg class="shapes" viewBox="0 0 532 750">
      <defs>
        <linearGradient id="catchTone" x1="0" y1="0" x2="1" y2="1">
          <stop offset="0" stop-color="#c9a9a0"/>
          <stop offset=".35" stop-color="#e6d8d3"/>
          <stop offset=".6" stop-color="#b88a80"/>
          <stop offset="1" stop-color="#d9c3bc"/>
        </linearGradient>
        <radialGradient id="troutTone" cx="45%" cy="40%" r="65%"><stop offset="0" stop-color="#f3f1ea"/><stop offset=".6" stop-color="#a7ada2"/><stop offset="1" stop-color="#6f7a6c"/></radialGradient>
        <radialGradient id="beefTone" cx="45%" cy="40%" r="65%"><stop offset="0" stop-color="#d6455a"/><stop offset="1" stop-color="#86192c"/></radialGradient>
        <radialGradient id="chilliTone" cx="45%" cy="40%" r="65%"><stop offset="0" stop-color="#f0663f"/><stop offset=".7" stop-color="#d0402f"/><stop offset="1" stop-color="#e8b23a"/></radialGradient>
      </defs>
      <path role="img" aria-label="Photo of a pile of fresh red mullet fish" d="M0,0 H532 V175 Q260,235 0,180Z" fill="url(#catchTone)"/>
      <path d="M0,180 Q260,235 532,175 V205 Q260,258 0,215Z" fill="var(--green)"/>
      <circle role="img" aria-label="Photo of whole trout with lemon slices" cx="90" cy="200" r="55" fill="url(#troutTone)" stroke="#fff" stroke-width="4"/>
      <circle role="img" aria-label="Photo of raw beef cuts with herbs" cx="262" cy="203" r="58" fill="url(#beefTone)" stroke="#fff" stroke-width="4"/>
      <circle role="img" aria-label="Photo of sliced meat with chillies" cx="435" cy="178" r="55" fill="url(#chilliTone)" stroke="#fff" stroke-width="4"/>
      <path d="M0,672 Q270,640 532,612 V750 H0Z" fill="var(--orange)"/>
    </svg>
    <h1 class="benefits-title">YOUR BENEFITS</h1>
    <ul class="benefits">
      <li><svg width="14" height="12" viewBox="0 0 14 12"><path d="M1,6 L5,10 L13,1" fill="none" stroke="var(--orange)" stroke-width="2.5"/></svg>Advertise your product online in 30 secs via your smart phone</li>
      <li><svg width="14" height="12" viewBox="0 0 14 12"><path d="M1,6 L5,10 L13,1" fill="none" stroke="var(--orange)" stroke-width="2.5"/></svg>Turn around stock faster</li>
      <li><svg width="14" height="12" viewBox="0 0 14 12"><path d="M1,6 L5,10 L13,1" fill="none" stroke="var(--orange)" stroke-width="2.5"/></svg>Larger exposure of your specials</li>
      <li><svg width="14" height="12" viewBox="0 0 14 12"><path d="M1,6 L5,10 L13,1" fill="none" stroke="var(--orange)" stroke-width="2.5"/></svg>Full training &amp; Support at no extra cost</li>
      <li><svg width="14" height="12" viewBox="0 0 14 12"><path d="M1,6 L5,10 L13,1" fill="none" stroke="var(--orange)" stroke-width="2.5"/></svg>No extra employees needed to open an online shop</li>
    </ul>
    <div class="sticker"><p>Sign Up Today<br><strong>ONLYU $150 pa</strong><br>FOR NEW<br>CUSTOMERS</p></div>
    <p class="note">A big point list a product online in 30 secs through your smart phone<br>don't know how to use a smart phone, full training and support will be<br>available to you anytime</p>
    <div class="cta">
      <h2>IF YOU ARE INTERESTED IN A FREE DEMO OR<br>SIGNING UP EMAIL</h2>
      <p>hello@catchcutmarket.com.au or call 0491 570 214</p>
      <p>www.catchcutmarket.com.au</p>
    </div>
  </section>

</div>
</body>
</html>
```